Business Cards for Law Office of Miriam T. Haskell

I need a business card for my new estate planning law firm. I have attached my logo. I would like a design that is professional but not too formal or stuffy.

Target Market(s)

Professionals (lawyers, doctors, businesswomen) between the age of 30 and 50 who are tech-savvy and educated.

Industry/Entity Type

Lawyer

Contact Information for Business Card

Miriam T. Haskell

582 E. 67th Street
9th Floor
New York, NY 10065

Phone: (855) 407-6218
Direct: (917) 563-0472
Email: Miriam@MiriamTHaskellLaw.example
www.MiriamTHaskellLaw.example

Font styles to use
Other font styles liked:
• Corbel

Requirements
Must have
• On the front:
• Miriam T. Haskell, Esq.
• Owner & Founder
• 582 E. 67th Street
• 9th Floor
• New York, NY 10065
• Phone: (855) 407-6218
• Direct: (917) 563-0472
• Email: miriam@miriamthaskelllaw.example
• www.miriamthaskelllaw.example
• On the back:
• LOGO
Nice to have
• I want it to be professional but not too formal or stuffy. Please choose colors that go with my logo.
Should not have
• I don't want TOO MUCH color. Some color is good, but not too much.

```html
<!DOCTYPE html>
<html lang="en">
<head>
<meta charset="utf-8">
<title>Business Cards – Law Office of Miriam T. Haskell</title>
<link rel="stylesheet" href="https://fonts.googleapis.com/css2?family=Marcellus&family=Tinos&display=swap">
<style>
  :root {
    --backdrop: #4a4a4a;
    --card: #ffffff;
    --plum: #7b2a7f;
    --orange: #f08127;
    --icon-fg: #ffffff;
  }
  html, body {
    margin: 0;
    padding: 0;
    width: 900px;
    height: 1200px;
    overflow: hidden;
    background: var(--backdrop);
  }
  .canvas {
    position: relative;
    width: 900px;
    height: 1200px;
  }
  .card {
    position: absolute;
    left: 80px;
    width: 739px;
    background: var(--card);
  }
  .card--front { top: 136px; height: 432px; }
  .card--back  { top: 631px; height: 430px; }

  /* Front */
  .holder-name {
    position: absolute;
    left: 48px;
    top: 226px;
    margin: 0;
    font-family: "Marcellus", serif;
    font-weight: 400;
    font-size: 23px;
    letter-spacing: 0.5px;
    color: var(--plum);
  }
  .holder-title {
    position: absolute;
    left: 48px;
    top: 257px;
    margin: 0;
    font-family: "Marcellus", serif;
    font-size: 16px;
    letter-spacing: 0.8px;
    color: var(--orange);
  }
  .title-rule {
    position: absolute;
    left: 239px;
    right: 49px;
    top: 269px;
    height: 1.5px;
    background: var(--orange);
  }
  .contact-list {
    position: absolute;
    left: 48px;
    top: 290px;
    margin: 0;
    padding: 0;
    list-style: none;
    font-family: "Tinos", serif;
    font-size: 16px;
    color: var(--plum);
  }
  .contact-list li {
    display: flex;
    align-items: center;
    height: 23px;
  }
  .contact-icon {
    width: 16px;
    height: 16px;
    margin-right: 13px;
    flex: none;
  }
  .address {
    position: absolute;
    right: 48px;
    top: 291px;
    margin: 0;
    font-family: "Tinos", serif;
    font-style: normal;
    font-size: 16px;
    line-height: 20.5px;
    text-align: right;
    color: var(--plum);
  }
  .accent-band {
    position: absolute;
    left: 0;
    bottom: 0;
    width: 100%;
    height: 13px;
    display: flex;
  }
  .accent-band span { flex: 1; }
  .accent-band .band-orange { background: var(--orange); }
  .accent-band .band-plum { background: var(--plum); }

  /* Back */
  .firm-name {
    position: absolute;
    left: 0;
    right: 0;
    top: 186px;
    margin: 0;
    text-align: center;
    font-family: "Marcellus", serif;
    font-weight: 400;
    font-size: 40px;
    letter-spacing: 0.5px;
    color: var(--plum);
  }
</style>
</head>
<body>
<main class="canvas">

  <section class="card card--front" aria-label="Business card front">
    <h1 class="holder-name">MIRIAM T. HASKELL, ESQ.</h1>
    <p class="holder-title">OWNER &amp; FOUNDER</p>
    <div class="title-rule"></div>

    <ul class="contact-list">
      <li>
        <svg class="contact-icon" viewBox="0 0 16 16" aria-hidden="true">
          <rect width="16" height="16" rx="3" fill="var(--orange)"/>
          <path d="M4.6 3.5l1.8 0 .8 2.3-1.1.9c.6 1.3 1.5 2.2 2.8 2.8l.9-1.1 2.3.8v1.8c0 .5-.4.9-.9.9C7.2 11.9 4.1 8.8 3.7 4.4c0-.5.4-.9.9-.9z" fill="var(--icon-fg)"/>
        </svg>
        (855) 407-6218
      </li>
      <li>
        <svg class="contact-icon" viewBox="0 0 16 16" aria-hidden="true">
          <rect width="16" height="16" rx="3" fill="var(--orange)"/>
          <path d="M4.6 3.5l1.8 0 .8 2.3-1.1.9c.6 1.3 1.5 2.2 2.8 2.8l.9-1.1 2.3.8v1.8c0 .5-.4.9-.9.9C7.2 11.9 4.1 8.8 3.7 4.4c0-.5.4-.9.9-.9z" fill="var(--icon-fg)"/>
        </svg>
        Direct: (917) 563-0472
      </li>
      <li>
        <svg class="contact-icon" viewBox="0 0 16 16" aria-hidden="true">
          <rect width="16" height="16" rx="3" fill="var(--orange)"/>
          <rect x="3.5" y="4.5" width="9" height="7" fill="none" stroke="var(--icon-fg)" stroke-width="1"/>
          <path d="M3.5 4.5L8 8.5l4.5-4" fill="none" stroke="var(--icon-fg)" stroke-width="1"/>
        </svg>
        miriam@miriamthaskelllaw.example
      </li>
      <li>
        <svg class="contact-icon" viewBox="0 0 16 16" aria-hidden="true">
          <rect width="16" height="16" rx="3" fill="var(--orange)"/>
          <circle cx="8" cy="8" r="4.5" fill="none" stroke="var(--icon-fg)" stroke-width="1"/>
          <ellipse cx="8" cy="8" rx="2" ry="4.5" fill="none" stroke="var(--icon-fg)" stroke-width="0.9"/>
          <path d="M3.5 8h9M4.2 5.8h7.6M4.2 10.2h7.6" stroke="var(--icon-fg)" stroke-width="0.8"/>
        </svg>
        www.miriamthaskelllaw.example
      </li>
    </ul>

    <address class="address">
      582 E. 67th Street<br>
      9th Floor<br>
      New York, NY 10065
    </address>

    <div class="accent-band" aria-hidden="true">
      <span class="band-orange"></span>
      <span class="band-plum"></span>
    </div>
  </section>

  <section class="card card--back" aria-label="Business card back">
    <h2 class="firm-name">Law Office of Miriam T. Haskell</h2>
  </section>

</main>
</body>
</html>
```